Banners for Project Management Conference Social Media SItes

We are part of an established global professional project management organisation (ZRV.org). We would be having our 21st project management conference in New Zealand this year and we are looking at a design of a series of banners that can be used across chatterly, blipster and workmesh. The design of banners should express the theme of the conference, "Shaping the Future".

Our conference logo is as attached. The conference logo must be in the banner image and form part of the inspiration to the banner design.

The banners fitting chatterly, blipster and workmesh should adhere to the banner sizing as follows.

1500x500px Blipster banner
851x315px Chatterly banner
646x220px Workmesh banner

They should be of the same design, with minor adjustments to fit the dimensions indicated. As they are web components, 72dpi, RGB are standard requirements for the images.

Deliverables: 1 jpg of each type of banner. (3 in total)

Just a heads-up: The blipster and chatterly banners would be partially blocked by its user-icon as shown in the two attached guide illustrations. Please make sure that the banner designed take into consideration of this and do not put in anything important (e.g. logo) in those spots.
Updates

Reason: Deadline extended because more interests have been registered. Thanks, guys.

Target Market(s)

Professional project managers, CEOs, Directors, managers in other fields.

Industry/Entity Type

Media

Requirements
Must have
• The conference logo must be part of the design of the banner. Would be great if the design can relate well with the logo.
Nice to have
• If stock images are needed to develop this banner, please inform.

```html
<!DOCTYPE html>
<html lang="en">
<head>
<meta charset="utf-8">
<title>ZRV.org Conference Banner – Shaping the Future</title>
<link rel="stylesheet" href="https://fonts.googleapis.com/css2?family=Roboto:wght@300;400;700;900&display=swap">
<style>
  :root {
    --paper: #f1efec;
    --paper-shade: #ddd8d3;
    --brand-red: #d8261f;
    --ink: #3a3a3a;
    --white: #ffffff;
    --orange: #e8812c;
    --orange-deep: #d9552a;
    --frame-line: #e9d6cf;
  }
  * { margin: 0; padding: 0; box-sizing: border-box; }
  html, body { width: 1200px; height: 400px; overflow: hidden; background: var(--paper); }
  .banner {
    position: relative;
    width: 1200px;
    height: 400px;
    overflow: hidden;
    font-family: "Roboto", Arial, sans-serif;
  }
  .city-backdrop {
    position: absolute; inset: 0;
    background:
      linear-gradient(90deg, rgba(255,255,255,.75) 0%, rgba(255,255,255,.35) 30%, rgba(255,255,255,0) 60%),
      linear-gradient(180deg, var(--paper) 0%, var(--paper-shade) 100%);
  }
  .brand-mark {
    position: absolute; left: 62px; top: 124px;
    display: flex; align-items: center; gap: 10px;
  }
  .brand-mark__dot {
    width: 22px; height: 22px; border-radius: 50%;
    background: var(--brand-red);
  }
  .brand-mark__name {
    font-size: 28px; font-weight: 700; color: var(--ink);
  }
  .theme-divider {
    position: absolute; left: 214px; top: 112px;
    width: 1px; height: 86px; background: var(--ink);
  }
  .theme-title {
    position: absolute; left: 222px; top: 123px;
    color: var(--ink); line-height: 1; font-weight: 300;
  }
  .theme-title__lead { display: block; font-size: 33px; font-weight: 300; letter-spacing: -0.5px; }
  .theme-title__line { display: block; margin-left: 37px; margin-top: 0; }
  .theme-title__small { font-size: 22px; font-weight: 300; letter-spacing: -0.5px; }
  .theme-title__accent { font-size: 36px; font-weight: 900; color: var(--brand-red); letter-spacing: -0.5px; }
  .visual-panel { position: absolute; left: 0; top: 0; }
  .contact-list { position: absolute; left: 467px; top: 32px; list-style: none; }
  .contact-item { position: relative; height: 36px; margin-bottom: 29px; }
  .contact-item__icon {
    position: absolute; left: 0; top: -1px;
    width: 38px; height: 38px; border-radius: 50%;
    border: 2px solid var(--brand-red); background: var(--white);
    display: flex; align-items: center; justify-content: center;
  }
  .contact-item__bar {
    position: absolute; left: 51px; top: 0; height: 36px;
    background: var(--brand-red); color: var(--white);
    font-size: 21px; font-weight: 300; line-height: 36px;
    padding-left: 8px; white-space: nowrap;
    clip-path: polygon(0 0, 100% 0, calc(100% - 28px) 100%, 0 100%);
  }
  .contact-item--address .contact-item__bar { width: 364px; }
  .contact-item--email .contact-item__bar { width: 296px; }
  .contact-item--phone .contact-item__bar { width: 236px; }
</style>
</head>
<body>
<main class="banner">
  <div class="city-backdrop" role="img" aria-label="Soft pale city skyline photograph in light greys"></div>

  <div class="brand-mark">
    <span class="brand-mark__dot"></span>
    <span class="brand-mark__name">ZRV.org</span>
  </div>

  <div class="theme-divider"></div>
  <h1 class="theme-title">
    <span class="theme-title__lead">Shaping</span>
    <span class="theme-title__line"><span class="theme-title__small">the</span><span class="theme-title__accent">Future</span></span>
  </h1>

  <svg class="visual-panel" width="1200" height="400" viewBox="0 0 1200 400">
    <defs>
      <linearGradient id="panelGradient" x1="0" y1="0" x2="1" y2="1">
        <stop offset="0" stop-color="#8b86b6"/>
        <stop offset="0.45" stop-color="#6d6b95"/>
        <stop offset="1" stop-color="#26313e"/>
      </linearGradient>
      <linearGradient id="posterGradient" x1="0" y1="0" x2="1" y2="1">
        <stop offset="0" stop-color="var(--orange)"/>
        <stop offset="0.5" stop-color="var(--orange-deep)"/>
        <stop offset="1" stop-color="var(--orange)"/>
      </linearGradient>
    </defs>
    <g role="img" aria-label="Upward view of city towers tinted purple and slate">
      <polygon points="904,11 1186,11 1186,387 526,387" fill="url(#panelGradient)"/>
      <polygon points="760,200 860,120 700,387 600,387" fill="#c9bfd9" opacity="0.45"/>
    </g>
    <rect class="event-poster" x="894" y="104" width="213" height="210" fill="url(#posterGradient)"
          role="img" aria-label="Orange and red festival event poster artwork"/>
  </svg>

  <ul class="contact-list">
    <li class="contact-item contact-item--address">
      <span class="contact-item__icon">
        <svg width="16" height="20" viewBox="0 0 16 20"><path d="M8 0C3.6 0 0 3.5 0 7.8 0 13.5 8 20 8 20s8-6.5 8-12.2C16 3.5 12.4 0 8 0z" fill="var(--brand-red)"/><circle cx="8" cy="7.5" r="2.8" fill="var(--white)"/></svg>
      </span>
      <span class="contact-item__bar">18 Harbour Lane, Wellbury</span>
    </li>
    <li class="contact-item contact-item--email">
      <span class="contact-item__icon">
        <svg width="20" height="14" viewBox="0 0 20 14"><rect width="20" height="14" fill="var(--brand-red)"/><polyline points="0,0 10,8 20,0" fill="none" stroke="var(--white)" stroke-width="1.4"/></svg>
      </span>
      <span class="contact-item__bar">hello@zrvsummit.org</span>
    </li>
    <li class="contact-item contact-item--phone">
      <span class="contact-item__icon">
        <svg width="18" height="18" viewBox="0 0 24 24"><path d="M6.6 10.8a15.2 15.2 0 0 0 6.6 6.6l2.2-2.2c.3-.3.7-.4 1-.2 1.1.4 2.3.6 3.6.6.6 0 1 .4 1 1V20c0 .6-.4 1-1 1A17 17 0 0 1 3 4c0-.6.4-1 1-1h3.5c.6 0 1 .4 1 1 0 1.3.2 2.5.6 3.6.1.3 0 .7-.2 1z" fill="var(--brand-red)"/></svg>
      </span>
      <span class="contact-item__bar">140 5512 7380</span>
    </li>
  </ul>
</main>
</body>
</html>
```